Business Card Design Project

Hi,
This is a simple contest. The logo for the back of the card is deigned. See attached files. The front of the card must have :

Directors Name: Dorian
Mob:
e-mail:
Postal Address:
Web Page Adress:

It may also add words: "Leaders in Construction Project Management Services"

Target Market(s)

Business & Home owners alike

Industry/Entity Type

Business

Requirements
Must have
• See details above and logo attached
Should not have
• Images other than logo

```html
<!DOCTYPE html>
<html lang="en">
<head>
<meta charset="utf-8">
<title>Ridgeway Projects Group — Business Card</title>
<link rel="stylesheet" href="https://fonts.googleapis.com/css2?family=Arimo:wght@400;700&display=swap">
<style>
  :root {
    --ink-black: #000000;
    --paper: #ffffff;
    --brand-blue: #009ddd;
    --text-blue: #0a9bd8;
    --steel-blue: #3e87a8;
  }
  * { margin: 0; padding: 0; box-sizing: border-box; }
  html, body {
    width: 960px; height: 1200px; overflow: hidden;
    background: var(--ink-black);
    font-family: "Arimo", Arial, sans-serif;
  }
  .canvas { position: relative; width: 960px; height: 1200px; }

  .card-front {
    position: absolute; left: 28px; top: 28px; width: 904px; height: 558px;
    background: var(--paper);
  }
  .holder-name {
    position: absolute; right: 97px; top: 52px;
    font-size: 41px; color: var(--steel-blue); line-height: 1; white-space: nowrap;
  }
  .holder-title {
    position: absolute; left: 472px; top: 99px; width: 366px;
    display: flex; justify-content: space-between;
    font-size: 25px; color: var(--text-blue); line-height: 1;
  }
  .front-brand {
    position: absolute; left: 70px; top: 181px; width: 267px; height: 266px;
    display: flex; flex-direction: column; justify-content: center; gap: 16px;
  }
  .front-brand .brand-square {
    width: 64px; height: 64px; background: var(--brand-blue);
  }
  .front-brand .brand-name {
    font-size: 34px; font-weight: 700; color: var(--brand-blue);
    line-height: 1.1; letter-spacing: 1px;
  }
  .contact-list { position: absolute; left: 353px; top: 181px; list-style: none; }
  .contact-item {
    position: absolute; left: 0; display: flex; align-items: center; white-space: nowrap;
  }
  .contact-icon {
    width: 53px; height: 53px; background: var(--steel-blue);
    display: flex; align-items: center; justify-content: center; flex: none;
  }
  .contact-text { margin-left: 17px; font-size: 25px; color: var(--text-blue); }
  .contact-item.phone  { top: 0; }
  .contact-item.email  { top: 71px; }
  .contact-item.postal { top: 142px; }
  .contact-item.web    { top: 212px; }

  .tagline-band {
    position: absolute; left: 0; bottom: 0; width: 904px; height: 49px;
    background: var(--brand-blue);
    display: flex; align-items: center; justify-content: center;
    font-size: 21px; color: var(--paper); letter-spacing: 3.2px; white-space: nowrap;
  }

  .card-back {
    position: absolute; left: 28px; top: 615px; width: 904px; height: 558px;
    background: var(--brand-blue);
  }
  .back-brand {
    position: absolute; left: 179px; top: 231px;
    display: flex; align-items: center; gap: 24px;
  }
  .back-brand .brand-square { width: 96px; height: 96px; background: var(--paper); }
  .back-brand .brand-name {
    font-size: 40px; font-weight: 700; color: var(--paper);
    line-height: 1.15; letter-spacing: 3px; white-space: nowrap;
  }
</style>
</head>
<body>
<main class="canvas">
  <section class="card-front">
    <h1 class="holder-name">Dorian Lastname</h1>
    <p class="holder-title"><span>D</span><span>I</span><span>R</span><span>E</span><span>C</span><span>T</span><span>O</span><span>R</span></p>

    <div class="front-brand">
      <div class="brand-square"></div>
      <p class="brand-name">RIDGEWAY<br>PROJECTS<br>GROUP</p>
    </div>

    <ul class="contact-list">
      <li class="contact-item phone">
        <span class="contact-icon">
          <svg width="30" height="42" viewBox="0 0 30 42"><rect x="4" y="1" width="22" height="40" rx="4" fill="#fff"/><rect x="7" y="7" width="16" height="25" fill="#3e87a8"/><circle cx="15" cy="36.5" r="2" fill="#3e87a8"/><rect x="11" y="3.5" width="8" height="1.5" fill="#3e87a8"/></svg>
        </span>
        <span class="contact-text">0000-000-0000</span>
      </li>
      <li class="contact-item email">
        <span class="contact-icon">
          <svg width="40" height="40" viewBox="0 0 40 40" fill="none" stroke="#fff" stroke-width="2.5"><path d="M4 17 L20 5 L36 17 V36 H4 Z"/><path d="M4 36 L16 25 M36 36 L24 25 M4 17 L20 29 L36 17"/><circle cx="20" cy="16" r="3.5"/><path d="M23.5 16 v2 a2 2 0 0 0 4 0 v-2 a7.5 7.5 0 1 0 -3 6"/></svg>
        </span>
        <span class="contact-text">emailhere@rpg.com</span>
      </li>
      <li class="contact-item postal">
        <span class="contact-icon">
          <svg width="38" height="32" viewBox="0 0 38 32"><rect x="1" y="1" width="36" height="30" fill="#fff"/><rect x="24" y="5" width="8" height="8" fill="#3e87a8"/><rect x="7" y="15" width="25" height="2" fill="#3e87a8"/><rect x="7" y="20" width="25" height="2" fill="#3e87a8"/><rect x="7" y="25" width="25" height="2" fill="#3e87a8"/></svg>
        </span>
        <span class="contact-text">Postal Adress Here</span>
      </li>
      <li class="contact-item web">
        <span class="contact-icon">
          <svg width="40" height="40" viewBox="0 0 40 40" fill="none" stroke="#fff" stroke-width="2.8"><circle cx="20" cy="20" r="17"/><ellipse cx="20" cy="20" rx="7.5" ry="17"/><path d="M3 20 H37 M6 11 H34 M6 29 H34"/></svg>
        </span>
        <span class="contact-text">www.ridgewayprojectsgroup.com</span>
      </li>
    </ul>

    <p class="tagline-band">"Leaders in Construction Project Management Services"</p>
  </section>

  <section class="card-back">
    <div class="back-brand">
      <div class="brand-square"></div>
      <p class="brand-name">RIDGEWAY<br>PROJECTS GROUP</p>
    </div>
  </section>
</main>
</body>
</html>
```